Wheels Bring Trade - Two sided invitation to encourage bike friendly businesses

Pedal Haven is a charitable trust who want to grow everyday bike use. One way to do that is help businesses understand that 'Wheels Bring Trade'. We want a postcard sized 'invitation' that bike users can give to their favourite businesses, inviting them to find out more about all the benefits of attracting bike users to their business and becoming a 'Pedal Haven Business'. We are currently finalising copy, so the attached is indicative but not final copy. The docx file is the words, the png is indicative of the type of infographic we might want to feature.
I'm also attaching a mock up of our window sticker for businesses, and some social shares featuring photographic images which we have available to use. This will give you an idea of our branding to date. Our extended branding concept (which we will use when we re-do our website) is based on icons, so I'm open to seeing icon focused designs also.
The feel needs to be inviting, credible, enticing, business like, noticeable, with a strong call to action.

Target Market(s)

Small business operators: retail, cafes, etc; also managers of larger chains such as supermarkets, gyms, etc.

Industry/Entity Type

Non Profit

Font styles to use
Serif
Other font styles liked:
• Logo is done in Raleway, so need compatible font.

Colors
9ccb3b

Requirements
Must have
• Two Sides
• Use the copy provided
• Strong call to action - visiting website
• Use our colours
• A6 sized cards
Nice to have
• Compelling images and/or infographic
• Consistency with circles / curves used in other branding.
Should not have
• Not bland, not something that will get lost on the recipients desk or counter.

```html
<!DOCTYPE html>
<html lang="en">
<head>
<meta charset="utf-8">
<title>Pedal Haven – Invitation Card</title>
<link rel="stylesheet" href="https://fonts.googleapis.com/css2?family=Raleway:wght@500;600;700&family=Lato:wght@400;700&family=Oswald:wght@500&display=swap">
<style>
  :root {
    --green: #9ccb3b;
    --green-deep: #3db54a;
    --charcoal: #3a3a3a;
    --grey-dark: #4b4b4b;
    --grey-mid: #7a7a7a;
    --ink: #151515;
    --paper: #ffffff;
    --paper-soft: #f4f4f4;
    --backdrop: #ecebe8;
  }
  * { box-sizing: border-box; margin: 0; padding: 0; }
  html, body { width: 1200px; height: 1200px; overflow: hidden; }
  body { background: var(--backdrop); font-family: "Lato", sans-serif; color: var(--ink); position: relative; }

  .card {
    position: absolute; top: 210px; width: 553px; height: 778px;
    background: linear-gradient(180deg, var(--paper) 0%, var(--paper-soft) 100%);
    box-shadow: 0 6px 18px rgba(0,0,0,0.25);
    overflow: hidden;
  }
  .card--front { left: 34px; }
  .card--back { left: 613px; }
  .card__art { position: absolute; inset: 0; width: 553px; height: 778px; }

  /* Front */
  .brand { position: absolute; left: 188px; top: 114px; display: flex; align-items: center; gap: 12px; }
  .brand__circle { width: 94px; height: 94px; border-radius: 50%; border: 4px solid var(--grey-dark); background: var(--paper); }
  .brand__name { font-family: "Raleway", sans-serif; font-weight: 600; font-size: 26px; line-height: 1.05; color: var(--green-deep); }

  .headline { position: absolute; left: 0; right: 0; top: 240px; text-align: center; font-family: "Raleway", sans-serif; font-weight: 600; color: var(--ink); }
  .headline__line { font-size: 30px; line-height: 1.2; display: block; }
  .headline__accent { display: flex; align-items: center; justify-content: center; gap: 18px; font-size: 38px; line-height: 1.1; color: var(--green-deep); margin: 2px 0; }
  .headline__accent::before, .headline__accent::after { content: ""; width: 66px; height: 2px; background: var(--green-deep); }

  .infographic { position: absolute; left: 41px; top: 405px; width: 471px; height: 300px; background: var(--paper); border: 1px solid #cfcfcf; box-shadow: 0 3px 8px rgba(0,0,0,0.25); }
  .infographic__till { position: absolute; left: 60px; width: 40px; height: 40px; border: 3px solid var(--ink); border-radius: 4px; }
  .infographic__till--car { top: 58px; }
  .infographic__till--bikes { top: 154px; }
  .infographic__area { position: absolute; left: 110px; font-size: 12px; line-height: 1; }
  .infographic__area--car { top: 75px; }
  .infographic__area--bikes { top: 171px; }
  .infographic__spend { position: absolute; left: 54px; font-family: "Oswald", sans-serif; font-weight: 500; font-size: 16px; line-height: 1; letter-spacing: -0.4px; white-space: nowrap; }
  .infographic__spend--car { top: 108px; }
  .infographic__spend--bikes { top: 204px; }
  .infographic__bracket { position: absolute; left: 158px; width: 6px; border: 2px solid var(--ink); border-left: none; }
  .infographic__bracket--car { top: 48px; height: 82px; }
  .infographic__bracket--bikes { top: 146px; height: 92px; }
  .infographic__divider { position: absolute; left: 164px; right: 70px; top: 139px; border-top: 2px dotted var(--grey-mid); }
  .infographic__car { position: absolute; left: 176px; top: 24px; width: 226px; height: 106px; border-radius: 40px 40px 12px 12px; background: linear-gradient(180deg, #e74a3a, #c8372a); }
  .infographic__bikes { position: absolute; left: 176px; top: 148px; width: 226px; height: 112px; border-radius: 8px; background: linear-gradient(180deg, #a6c8e8, #4a6f96); }
  .infographic__source { position: absolute; left: 0; right: 0; bottom: 18px; text-align: center; font-size: 6.5px; font-weight: 700; }

  .front-footer { position: absolute; left: 0; right: 0; top: 737px; height: 34px; display: flex; align-items: center; justify-content: center; color: var(--paper); font-family: "Raleway", sans-serif; font-weight: 500; font-size: 16px; letter-spacing: 3.2px; }

  /* Back */
  .why-title { position: absolute; left: 41px; top: 118px; font-family: "Raleway", sans-serif; font-weight: 700; font-size: 26px; color: var(--green); }
  .benefits { position: absolute; left: 41px; top: 178px; width: 470px; list-style: none; }
  .benefit { position: relative; padding-left: 36px; font-size: 15.5px; line-height: 1.25; color: var(--ink); }
  .benefit + .benefit { margin-top: 15px; }
  .benefit__icon { position: absolute; left: 0; top: -4px; width: 31px; height: 31px; }
  .study { position: absolute; left: 20px; right: 20px; top: 447px; text-align: center; font-size: 19px; line-height: 1.22; }
  .callout { position: absolute; left: 40px; top: 557px; width: 472px; height: 63px; border: 1.5px solid var(--grey-dark); border-radius: 16px; display: flex; align-items: center; justify-content: center; text-align: center; font-size: 19px; line-height: 1.25; color: var(--ink); }
  .callout__accent { color: var(--green); font-weight: 700; }
  .cta { position: absolute; left: 40px; top: 701px; color: var(--ink); }
  .cta__lead { font-size: 20px; }
  .cta__link { color: var(--paper); }
  .cta__sub { font-size: 16px; margin-top: 2px; }
</style>
</head>
<body>

<section class="card card--front" aria-label="Front of invitation card">
  <svg class="card__art" viewBox="0 0 553 778" aria-hidden="true">
    <defs>
      <linearGradient id="headGrey" x1="0" y1="0" x2="0" y2="1">
        <stop offset="0" stop-color="#3f3f3f"/>
        <stop offset="1" stop-color="#7d7d7d"/>
      </linearGradient>
      <linearGradient id="footGreen" x1="0" y1="0" x2="0" y2="1">
        <stop offset="0" stop-color="#b3db5c"/>
        <stop offset="1" stop-color="#8cc034"/>
      </linearGradient>
    </defs>
    <path d="M0 0 H553 V48 C470 10 380 20 300 45 C200 78 100 108 0 103 Z" fill="url(#headGrey)"/>
    <path d="M0 107 C100 112 200 82 300 49 C380 24 470 14 553 52" fill="none" stroke="var(--green)" stroke-width="4"/>
    <path d="M0 570 C80 650 220 690 380 690 C460 690 520 670 553 650 V737 H0 Z" fill="url(#footGreen)"/>
    <path d="M0 565 C80 645 220 684 380 684 C460 684 520 664 553 644" fill="none" stroke="var(--charcoal)" stroke-width="5"/>
    <rect x="0" y="737" width="553" height="34" fill="var(--charcoal)"/>
    <rect x="0" y="771" width="553" height="7" fill="var(--green)"/>
  </svg>

  <div class="brand">
    <span class="brand__circle"></span>
    <span class="brand__name">Pedal<br>Haven</span>
  </div>

  <h1 class="headline">
    <span class="headline__line">Why make biking customers</span>
    <span class="headline__accent">and their $$$</span>
    <span class="headline__line">Welcome at your business?</span>
  </h1>

  <figure class="infographic">
    <span class="infographic__till infographic__till--car" aria-hidden="true"></span>
    <span class="infographic__area infographic__area--car">13m2</span>
    <span class="infographic__spend infographic__spend--car">$27.00 per hour</span>
    <span class="infographic__bracket infographic__bracket--car"></span>
    <div class="infographic__car" role="img" aria-label="Illustration of a red car parked in one car space"></div>
    <span class="infographic__divider"></span>
    <span class="infographic__till infographic__till--bikes" aria-hidden="true"></span>
    <span class="infographic__area infographic__area--bikes">13m2</span>
    <span class="infographic__spend infographic__spend--bikes">$97.20 per hour</span>
    <span class="infographic__bracket infographic__bracket--bikes"></span>
    <div class="infographic__bikes" role="img" aria-label="Illustration of six bikes parked in the same space, each tagged $16.20 per hour"></div>
    <figcaption class="infographic__source">Retail Spend per hour, Lygon Street, Carlton, Melbourne Australia; Dana Reeve</figcaption>
  </figure>

  <div class="front-footer">www.pedalhaven.org</div>
</section>

<section class="card card--back" aria-label="Back of invitation card">
  <svg class="card__art" viewBox="0 0 553 778" aria-hidden="true">
    <defs>
      <linearGradient id="headGreyB" x1="0" y1="0" x2="0" y2="1">
        <stop offset="0" stop-color="#3f3f3f"/>
        <stop offset="1" stop-color="#7d7d7d"/>
      </linearGradient>
      <linearGradient id="footGreenB" x1="0" y1="0" x2="0" y2="1">
        <stop offset="0" stop-color="#a6d24a"/>
        <stop offset="1" stop-color="#92c43a"/>
      </linearGradient>
    </defs>
    <path d="M0 0 H553 V102 C450 108 350 80 250 55 C160 32 70 30 0 55 Z" fill="url(#headGreyB)"/>
    <path d="M0 58 C70 34 160 36 250 59 C350 84 450 112 553 106" fill="none" stroke="var(--green)" stroke-width="4"/>
    <path d="M0 670 C120 640 250 645 380 675 C450 690 510 680 553 670 V778 H0 Z" fill="url(#footGreenB)"/>
    <path d="M0 672 C120 642 250 647 380 677 C450 692 510 682 553 672" fill="none" stroke="var(--charcoal)" stroke-width="6"/>
    <path d="M0 670 C120 652 250 660 380 690 C450 705 510 700 553 685 V680 C510 692 450 697 380 683 C250 653 120 646 0 666 Z" fill="var(--charcoal)" opacity="0.6"/>
    <rect x="0" y="770" width="553" height="8" fill="var(--charcoal)"/>
  </svg>

  <h2 class="why-title">Why welcome bikes?</h2>

  <ul class="benefits">
    <li class="benefit">
      <svg class="benefit__icon" viewBox="0 0 31 31" aria-hidden="true"><circle cx="15.5" cy="15.5" r="15" fill="var(--grey-dark)"/><text x="15.5" y="21" text-anchor="middle" font-size="15" font-weight="700" fill="var(--green)" font-family="Lato, sans-serif">$</text></svg>
      Biking customers spend $$$ where parking’s easy.
    </li>
    <li class="benefit">
      <svg class="benefit__icon" viewBox="0 0 31 31" aria-hidden="true"><circle cx="15.5" cy="15.5" r="15" fill="var(--grey-dark)"/><circle cx="10" cy="19" r="4.5" fill="none" stroke="var(--green)" stroke-width="1.6"/><circle cx="21" cy="19" r="4.5" fill="none" stroke="var(--green)" stroke-width="1.6"/><path d="M10 19 L14 12 H19 L21 19 M14 12 L16 19" fill="none" stroke="var(--green)" stroke-width="1.6"/></svg>
      They spend $$$ locally as they must carry what they buy.
    </li>
    <li class="benefit">
      <svg class="benefit__icon" viewBox="0 0 31 31" aria-hidden="true"><circle cx="15.5" cy="15.5" r="15" fill="var(--grey-dark)"/><circle cx="10" cy="19" r="4.5" fill="none" stroke="var(--green)" stroke-width="1.6"/><circle cx="21" cy="19" r="4.5" fill="none" stroke="var(--green)" stroke-width="1.6"/><path d="M10 19 L15 13 L21 19" fill="none" stroke="var(--green)" stroke-width="1.6"/></svg>
      Biking customers move slower, so see what your business offers.
    </li>
    <li class="benefit">
      <svg class="benefit__icon" viewBox="0 0 31 31" aria-hidden="true"><circle cx="15.5" cy="15.5" r="15" fill="var(--grey-dark)"/><path d="M15.5 7 V24 M9 10 H22" fill="none" stroke="var(--green)" stroke-width="1.8"/><circle cx="15.5" cy="24" r="1.8" fill="var(--green)"/></svg>
      They tell friends where’s good to park and shop, where they feel welcome.
    </li>
    <li class="benefit">
      <svg class="benefit__icon" viewBox="0 0 31 31" aria-hidden="true"><circle cx="15.5" cy="15.5" r="15" fill="var(--grey-dark)"/><path d="M15.5 23 C9 18 8 12 12 10 C14 9 15.5 11 15.5 12 C15.5 11 17 9 19 10 C23 12 22 18 15.5 23 Z" fill="var(--green)"/></svg>
      You’re helping people be environmentally, budget and heart friendly – and they’ll you for it.
    </li>
  </ul>

  <p class="study">A Melbourne study showed swapping a car park<br>for six bike parks could increase the space’s retail spend<br>from $27 to $97.20 an hour.</p>

  <p class="callout"><span><span class="callout__accent">Just think – every</span> bike parked by someone else’s <span class="callout__accent">business could have been your customer.</span></span></p>

  <div class="cta">
    <p class="cta__lead">See <span class="cta__link">pedalhaven.org.nz</span></p>
    <p class="cta__sub">to see how you can become a Pedal Haven business.</p>
  </div>
</section>

</body>
</html>
```